Super elegant, crisp & clean Business card design required

We recently upgraded our branding - which is on our website - tavorelstudio.com

I would like a simple, yet elegant, clean business card design please.

The font of my logo is Cinzel - and because of the natural colour - it's best to have this on a black background.

I would like to have the back of the business card - with simply my logo.

PLEASE DO NOT SUBMIT A COMPLICATED / UNCLEAN DESIGN

Industry/Entity Type

Business

Contact Information for Business Card

Dalvik Ostrander Photography

Font styles to use
Other font styles liked:
• Cinzel

Requirements
Must have
• A backpage with nothing but my logo
• Simple design - stands out
Should not have
• Colour that dont align with my logo
• Over complicated '/ non symmetrical design

```html
<!DOCTYPE html>
<html lang="en">
<head>
<meta charset="utf-8">
<title>Dalvik Ostrander Photography – Business Card</title>
<link rel="stylesheet" href="https://fonts.googleapis.com/css2?family=Cinzel:wght@400&family=Didact+Gothic&display=swap">
<style>
  :root {
    --backdrop: #cdc3b1;
    --card: #1c1c1b;
    --gold: #8d7157;
    --gold-soft: rgba(141, 113, 87, 0.55);
  }
  * { margin: 0; padding: 0; box-sizing: border-box; }
  html, body {
    width: 1200px;
    height: 754px;
    overflow: hidden;
    background: var(--backdrop);
  }
  .canvas {
    position: relative;
    width: 1200px;
    height: 754px;
  }
  .card {
    position: absolute;
    top: 242px;
    width: 459px;
    height: 255px;
    background: var(--card);
    color: var(--gold);
    text-align: center;
  }
  .card--front { left: 120px; }
  .card--back { left: 624px; }

  .wordmark {
    position: absolute;
    left: 0;
    right: 0;
    font-family: "Cinzel", serif;
    font-weight: 400;
  }
  .wordmark__name {
    display: block;
    font-size: 18px;
    letter-spacing: 0.5px;
    line-height: 1;
  }
  .wordmark__trade {
    display: block;
    margin-top: 4px;
    font-size: 8px;
    letter-spacing: 6.4px;
    line-height: 1;
    padding-left: 6px;
  }
  .card--front .wordmark { top: 87px; }
  .card--back .wordmark { top: 155px; }

  .divider {
    position: absolute;
    top: 135px;
    left: 85px;
    width: 289px;
    height: 1px;
    background: linear-gradient(to right, transparent, var(--gold-soft) 30%, var(--gold-soft) 70%, transparent);
  }
  .contact {
    position: absolute;
    top: 152px;
    left: 0;
    right: 0;
    font-family: "Didact Gothic", sans-serif;
    font-size: 11.5px;
    line-height: 14px;
  }
  .contact__label { font-weight: 700; }

  .brand-dot {
    position: absolute;
    top: 76px;
    left: 50%;
    width: 40px;
    height: 40px;
    margin-left: -20px;
    border: 1px solid var(--gold);
    border-radius: 50%;
  }
</style>
</head>
<body>
<main class="canvas">
  <section class="card card--front" aria-label="Business card front">
    <h1 class="wordmark">
      <span class="wordmark__name">Dalvik Ostrander</span>
      <span class="wordmark__trade">Photography</span>
    </h1>
    <div class="divider"></div>
    <p class="contact">
      <span class="contact__label">T:</span> 07940218365 ·<span class="contact__label">E:</span> info@tavorelstudio.com<br>
      www.tavorelstudio.com
    </p>
  </section>

  <section class="card card--back" aria-label="Business card back">
    <span class="brand-dot"></span>
    <p class="wordmark">
      <span class="wordmark__name">Dalvik Ostrander</span>
      <span class="wordmark__trade">Photography</span>
    </p>
  </section>
</main>
</body>
</html>
```